Thabeni Academy one-page profile

I need to develop a professionally designed "one-pager" for a new independent school opening in the Mavuso Township in South Africa in 2015. Mavuso is one of the poorest communities in South Africa and our aim is to bring a university preparatory education to this community. The school will open with kindergarten students and will expand each year until we reach grade 12. I would like for the file to be in a format that I can easily edit in the event that the information that I provide in the attachment changes or should I choose to utilize the format for an additional flyer.

The document needs to be designed as an A4 paper sized document as opposed to the standard size used in the United States.

I like the format of the following document:
http://www.brelvonschools.org/pdfs/11.30.2012%20BNQS%20Tutoring%20One%20Pager.pdf
http://www.prindlework.com/images/150_Teacher_recruitment_flyer.jpg
http://slatehouse.org/2013/01/18/BRON%2520TQGS%2520Lottery%2520Information_English%2520Flyer%5B1%5D.jpg
Updates

I edited the attached Thabeni Academy one page profile by altering it slightly and cutting out some unnecessary wording.  Please view to make changes.

Target Market(s)

The target market for this piece are potential funders and partners.

Industry/Entity Type

University

Requirements
Must have
• The design must use the Thabeni Academy colors and fonts as outlined in the branding guide. The design must look professional and must give the impression of a stellar private school.
Should not have
• Clip art

```html
<!DOCTYPE html>
<html lang="en">
<head>
<meta charset="utf-8">
<title>Thabeni Academy — One-Page Profile</title>
<link href="https://fonts.googleapis.com/css2?family=Jost:wght@400;500&family=Open+Sans:wght@600;700&display=swap" rel="stylesheet">
<style>
:root{
  --blue:#1f6fb5;
  --blue-deep:#1a5b9c;
  --sky:#d8ecf8;
  --sky-soft:#eef7fc;
  --text:#333a40;
  --orange:#f6921e;
  --tile-blue:#1c75bc;
  --magenta:#b3166e;
  --green:#8dc63f;
  --ink:#231f20;
  --white:#ffffff;
}
*{margin:0;padding:0;box-sizing:border-box}
html,body{width:874px;height:1200px;overflow:hidden;background:#f2f2f2}
.page{position:relative;width:874px;height:1200px;overflow:hidden;background:var(--white);font-family:"Jost",sans-serif;color:var(--text)}
.header-swoosh{position:absolute;top:0;left:0;width:874px;height:230px}
.brand{position:absolute;left:46px;top:58px;display:flex;align-items:center;gap:14px}
.brand-dot{width:64px;height:64px;border-radius:50%;background:var(--blue)}
.brand-name{font-size:30px;font-weight:500;color:var(--blue);line-height:1}
.tagline{position:absolute;left:124px;top:134px;font-size:12px;color:var(--blue-deep)}
.site-url{position:absolute;right:42px;top:98px;font-size:25px;color:var(--blue)}
.photo-band{position:absolute;top:188px;left:0;width:874px;height:270px}
.photos{position:absolute;top:208px;left:46px;width:782px;height:220px;display:flex;gap:4px}
.photo{flex:1}
.photo-family{background:linear-gradient(135deg,#5a5a5a,#c9c9c9)}
.photo-reader{background:linear-gradient(135deg,#c9e3f3,#8a6a52)}
.photo-toddler{background:linear-gradient(135deg,#e5c43a,#c0392b 60%,#6b4a3a)}
.content{position:absolute;top:452px;left:46px;width:786px;font-size:13.2px;line-height:1.38}
.section-title{font-size:13.5px;color:var(--blue);text-transform:uppercase;margin-top:5px}
.content p{margin-bottom:2px}
.model-row{display:flex;gap:18px}
.model-text{flex:1}
.features{list-style:none;margin:2px 0 2px 30px}
.features li{position:relative;padding-left:14px}
.features li::before{content:"";position:absolute;left:0;top:7px;width:6px;height:6px;border-radius:50%;background:var(--blue)}
.components{display:grid;grid-template-columns:162px 162px;grid-template-rows:112px 112px;gap:4px;margin-top:22px;flex:none}
.tile{display:flex;flex-direction:column;align-items:center;font-family:"Open Sans",sans-serif;font-weight:700;font-size:11.5px;color:var(--white);text-align:center;padding-top:5px;line-height:1.2}
.tile svg{margin-top:auto;margin-bottom:12px}
.tile-justice{background:var(--orange)}
.tile-planning{background:var(--tile-blue)}
.tile-literacy{background:var(--magenta)}
.tile-data{background:var(--green)}
.leader-label{color:var(--blue);text-transform:uppercase}
.footer-wave{position:absolute;left:0;bottom:0;width:874px;height:150px}
.contact-phone{position:absolute;left:56px;bottom:36px;font-size:15px;line-height:1.25;color:var(--white)}
.contact-email{position:absolute;right:50px;bottom:42px;font-size:16px;color:var(--white)}
</style>
</head>
<body>
<div class="page">
  <svg class="header-swoosh" viewBox="0 0 874 230" aria-hidden="true">
    <path d="M300 0 H874 V200 C760 170 620 160 520 110 C440 70 380 30 300 0Z" fill="var(--sky-soft)"/>
    <path d="M420 0 H874 V150 C760 120 650 110 560 60 C500 30 460 10 420 0Z" fill="var(--sky)"/>
  </svg>

  <div class="brand">
    <div class="brand-dot"></div>
    <div class="brand-name">Thabeni Academy</div>
  </div>
  <div class="tagline">Set Your Dreams Free</div>
  <div class="site-url">www.siyakhafoundation.org</div>

  <svg class="photo-band" viewBox="0 0 874 270" aria-hidden="true">
    <path d="M0 22 C200 0 420 2 874 20 V250 C600 236 300 262 0 270Z" fill="var(--blue)"/>
  </svg>
  <div class="photos">
    <div class="photo photo-family" role="img" aria-label="Photo of a mother and young child reading together"></div>
    <div class="photo photo-reader" role="img" aria-label="Photo of a young boy reading a book at a desk"></div>
    <div class="photo photo-toddler" role="img" aria-label="Photo of a toddler reading among colourful classroom chairs"></div>
  </div>

  <main class="content">
    <h2 class="section-title">Who are we</h2>
    <p>Thabeni Academy will open its doors in January 2015 as the first Grade R- 12 university preparatory school in Mavuso. Admission to Thabeni Academy is on a first come, first serve basis and the school will serve Grade R students in 2015 and will add a new grade each year.</p>
    <p>Thabeni Academy is a proud member of The Open Sky Network of Schools, an organization, founded in the United States, committed to building a global network of transformational breakthrough schools.</p>

    <h2 class="section-title">Our community</h2>
    <p>Mavuso is a historic area located in the Gauteng Province in South Africa with several notable leaders residing in Mavuso at some point in their journey, including President Themba Nkosi and former First Lady Lindiwe Sithole. Mavuso is a community full of promise but is considered one of the most economically disenfranchised urban communities in the country. The average household income in Mavuso is under R5000.00 per month and an estimated population of 500,000 people live on 1 square mile of land.</p>

    <h2 class="section-title">Our model</h2>
    <div class="model-row">
      <div class="model-text">
        <p>Thabeni Academy has several unique features aimed to put all students on the path to university:</p>
        <ul class="features">
          <li>University preparatory curriculum and learning environment</li>
          <li>Highly qualified, caring, and passionate educators and staff</li>
          <li>Extended School Day</li>
          <li>Dual Language Programme (English and Zulu)</li>
          <li>Creative Arts and movement classes</li>
          <li>Technology Integration across subject areas</li>
          <li>Extra-murals built into the school day</li>
        </ul>
        <h2 class="section-title">Core components</h2>
        <p>At Thabeni Academy, we have outlined four core components that will be prioritized, with each area providing an avenue for achieving our mission of ensuring that all students are prepared with the academic and character skills that they need to be successful in university.</p>
      </div>
      <div class="components">
        <div class="tile tile-justice">Social Justice Foundation
          <svg width="70" height="62" viewBox="0 0 70 62" aria-hidden="true"><g fill="var(--ink)"><rect x="33" y="4" width="4" height="50"/><rect x="8" y="10" width="54" height="3"/><rect x="20" y="54" width="30" height="5"/><path d="M2 36 H26 A12 6 0 0 1 2 36Z"/><path d="M44 36 H68 A12 6 0 0 1 44 36Z"/></g><g stroke="var(--ink)" stroke-width="1.5"><path d="M14 12 L3 36 M14 12 L25 36 M56 12 L45 36 M56 12 L67 36" fill="none"/></g></svg>
        </div>
        <div class="tile tile-planning">Standard Based Unit and Lesson Planning
          <svg width="60" height="58" viewBox="0 0 60 58" aria-hidden="true"><path d="M44 4 L56 16 L20 52 L6 56 L10 42Z" fill="var(--ink)"/><path d="M40 8 L52 20" stroke="var(--tile-blue)" stroke-width="3"/></svg>
        </div>
        <div class="tile tile-literacy">Literacy Focus
          <svg width="74" height="56" viewBox="0 0 74 56" aria-hidden="true"><path d="M4 8 C16 2 28 4 35 10 V52 C28 46 16 44 4 50Z M70 8 C58 2 46 4 39 10 V52 C46 46 58 44 70 50Z" fill="none" stroke="var(--ink)" stroke-width="6"/></svg>
        </div>
        <div class="tile tile-data">Data Driven Instruction
          <svg width="64" height="56" viewBox="0 0 64 56" aria-hidden="true"><g fill="var(--ink)"><rect x="4" y="50" width="56" height="4"/><rect x="4" y="8" width="4" height="46"/><rect x="14" y="30" width="8" height="18"/><rect x="26" y="24" width="8" height="24"/><rect x="38" y="28" width="8" height="20"/><rect x="50" y="14" width="8" height="34"/></g><path d="M14 24 L30 14 L42 20 L58 6" stroke="var(--ink)" stroke-width="3" fill="none"/></svg>
        </div>
      </div>
    </div>

    <p><span class="leader-label">Our school leader:</span> Naledi Mokoena-Hart is passionate about education and social justice and has been a contributing writer for Learning Southern Africa and Reimagining Classrooms and in 2012 Naledi gave an IdeasX talk on the importance of an education steeped in social justice. Naledi is excited about the opportunity to learn and serve the Mavuso Township and is one of the organizers for IdeasXMavuso. In 2013, Naledi completed the highly selective Lumen Global Fellowship in the United States which is a specialized programme that prepares fellows to found and lead high performing schools in under-served communities. Prior to establishing the Thabeni Academy, Naledi taught middle school humanities for seven years and worked as an education programme coordinator. Naledi holds an MS Degree in Education Policy from Lakeshore State University, where she was an Advanced Opportunity Fellow and a BA in education from Hillcrest College.</p>
  </main>

  <svg class="footer-wave" viewBox="0 0 874 150" aria-hidden="true">
    <path d="M0 40 C260 10 520 30 874 0 V150 H0Z" fill="var(--sky)"/>
    <path d="M0 52 C300 30 560 60 874 26 V150 H0Z" fill="var(--blue)"/>
    <path d="M560 150 C620 100 700 60 874 40 V150Z" fill="var(--tile-blue)"/>
  </svg>
  <div class="contact-phone">If you have questions, please contact a member of our team<br>at +27 71-308-4826</div>
  <div class="contact-email">info@siyakhafoundation.org</div>
</div>
</body>
</html>
```